Design a cool print brochure for an NGO / Give your work a global impact!!

Hi,
I provide a full design brief (below, please scroll) and a mood board (attached) to help you visualize inside my head.. ;-)
I am also available to help and have worked many years in advertising; we will understand each other.
Objective:
To design an A4 folded in two presentation brochure for a non-profit consulting agency called Vantor.
Vantor works in sustainability and international development = working with NGO’s, governments and private sector on global issues such as global warming, education for all etc.
Strategy:
This document is a first step in developing a communication strategy. It will be distributed during a major international event called the Meridian Outreach Forum.
Objective:
The double objective of the brochure is:
a) to inform the recipient of what Vantor is, in the shortest time possible.
b) to showcase relevant projects to demonstrate Vantor experience and expertise.
Target:
Main target:
Existing Vantor contacts, such as members of development organizations, NGOs, private sector foundations (CSR), regional networks and other development actors.
NB: the main target already has a certain awareness of Vantor: we will try to minimize text to maximize visual impact and readability.
Secondary target:
Vantor will also distribute the brochure to new prospects of interest during the Meridian Forum.
Timing:
We will need to finalize the design and have the files by June 1st to allow time for print before the event.
Content:
The document should be concise, highly readable (no clutter) and include:
1. text (that we will provide)
and
2. visual elements such as images, shapes and info-graphics (that is you).
NB: Vantor does not have its own image bank; photos will be provided by you.
Format:
A4 folded in half - 4pp A5 - PORTRAIT FORMAT) with an impactful visual in the front, logo, title and headline (please see examples in the mood board attached).
Design elements:
Vantor does not have yet a visual identity (please see: http://vantor.org) so there is room for creativity and no graphic chart to follow.
The sector of consulting in international development is rather conservative but our intention is to be disruptive and create a “Wow” effect. We count on you for that!
Therefore, the design should be “structured”, “organized”, “uncluttered” but also “modern”, “impactful”, “highly visual” (think infographic or mind map to describe our services and projects).
Please, take the time to see the attached presentation: I give you guidelines and examples of what we want and what we like.
We are looking forward to seeing your work and I am available for comments, questions and support.
Thank you.
RK
Target Market(s)
The full brief is in the project description: please, scroll through it.
The target market is : our existing clients base, working in sustainable development (read: NGO and United Nations people)
Industry/Entity Type
Ngo
Font styles to use
Requirements
Must have
- - Design and color elements: please, no black and white. Our company website is in black and white and without graphics; we want the brochure to break away from that and start creating our brand identity; so please, show us colors and desing elements (shapes, backgrounds, etc).
- You have a chance to showcase your talent in terms of visual identity: what lines, forms, layout and colors can you come up with and apply throughout the brochure and serve as the visual identity of Vantor?
- The structure of the document should be:
- - Front cover: design elements + impacful photo (see mood board example attached) +our logo + this headline: "Collective action for sustainable development and impact"
- - Inside front: a graphic representation of "Our Services": such as core activity in the center circle and satellite circles for the services we offer.
- - Inside back:
- 1. Icons and text boxes for "Our projects"
- 2. A world map of the countries where we have worked. Full list of countries is here:
- http://vantor.org/experience-1
- - Back cover: our contact + logos of partners.
- Our partners are listed here:
- Please use their original logos (ie, in color).
- The design we will select will serve as a basis for a graphic chart...so more work to come...word to the wise ;)
- Please check out our website vantor.org to see what we do etc.
Nice to have
- Icons to reflect our services: what icons can you come up with to describe "training services", "building networks" or "program management"?
- I give examples in the mood board.
Should not have
- We are open to creativity and want to generate a "Wow" effect.
- Just note that the sector is rather conservative so flashy colors and cartoon like characters should be avoided. Think "earth, global change, United Nations, climate" without going too green (it's overdone). ;-)
- Make us stand out in the NGO world
- Now you.

```html
<!DOCTYPE html>
<html lang="en">
<head>
<meta charset="utf-8">
<title>Vantor — Services and Projects Spread</title>
<link rel="stylesheet" href="https://fonts.googleapis.com/css2?family=Roboto:wght@300;400;700&family=Roboto+Condensed:wght@400;700&display=swap">
<style>
  :root {
    --navy: #1b2a4a;
    --navy-deep: #16223d;
    --ink: #1e2b45;
    --text: #333c4d;
    --white: #ffffff;
    --paper: #fbfbfb;
    --stage: #e9e7e3;
    --earth-blue: #3f7fb5;
    --map-green: #a4cf45;
    --map-green-soft: #c6df86;
    --map-teal: #6fa9b0;
    --map-sea: #eef3f2;
    --icon-grey: #9aa3ad;
    --rule: #b9c0cc;
  }
  * { box-sizing: border-box; margin: 0; padding: 0; }
  html, body { width: 1200px; height: 800px; overflow: hidden; }
  body {
    background: var(--stage);
    font-family: "Roboto", Arial, sans-serif;
    color: var(--text);
    position: relative;
  }
  .spread {
    position: absolute; left: 64px; top: 20px;
    width: 1072px; height: 760px;
    display: flex;
    box-shadow: 0 6px 24px rgba(0,0,0,.18);
  }
  .page { position: relative; width: 536px; height: 760px; overflow: hidden; background: var(--paper); }
  .page-services { border-right: 1px solid #d6d6d6; }

  .page-title {
    position: absolute; left: 24px; top: 44px;
    font-weight: 300; font-size: 34px; letter-spacing: .5px;
    color: var(--navy);
    padding-bottom: 4px;
    border-bottom: 1px solid var(--rule);
    width: 300px;
  }
  .page-projects .page-title { color: var(--white); border-bottom-color: rgba(255,255,255,.35); left: 18px; }

  /* Services mind map */
  .globe {
    position: absolute; left: 180px; top: 185px; width: 186px; height: 186px; border-radius: 50%;
    background: radial-gradient(circle at 38% 35%, #8ec3e8 0%, var(--earth-blue) 45%, #2b5f8c 75%, #6f9f4a 100%);
  }
  .service-icon {
    position: absolute; width: 44px; height: 44px; border-radius: 50%;
    background: radial-gradient(circle, #e4e7ea 0%, var(--icon-grey) 100%);
  }
  .service { position: absolute; }
  .service h3 {
    font-family: "Roboto Condensed", Arial, sans-serif;
    font-weight: 700; font-size: 11.5px; line-height: 1.15;
    color: var(--ink); text-transform: uppercase; margin-bottom: 3px;
  }
  .service p { font-size: 9.5px; line-height: 1.3; color: var(--text); }
  .service.align-right { text-align: right; }

  .services-band {
    position: absolute; left: 0; top: 537px; width: 536px; height: 223px;
    background: var(--navy); padding: 20px 22px;
  }
  .services-band p { color: var(--white); font-size: 11px; line-height: 1.55; }

  /* Projects */
  .projects-band {
    position: absolute; left: 0; top: 0; width: 536px; height: 304px;
    background: var(--navy-deep); padding: 92px 18px 0;
  }
  .projects-band p { color: var(--white); font-size: 11.5px; line-height: 1.55; margin-bottom: 12px; }
  .stats { position: absolute; top: 340px; left: 14px; display: flex; align-items: baseline; gap: 28px; }
  .stat { display: flex; align-items: baseline; gap: 8px; color: var(--ink); }
  .stat-figure { font-family: "Roboto Condensed", Arial, sans-serif; font-weight: 700; font-size: 52px; line-height: 1; }
  .stat-label { font-family: "Roboto Condensed", Arial, sans-serif; font-size: 20px; letter-spacing: .5px; }
  .world-map {
    position: absolute; left: 12px; top: 402px; width: 510px; height: 262px;
    background:
      linear-gradient(180deg, rgba(238,243,242,0) 0%, rgba(238,243,242,0) 70%, var(--map-sea) 100%),
      linear-gradient(100deg, var(--map-teal) 0%, var(--map-green-soft) 28%, var(--map-sea) 46%, var(--map-green) 62%, var(--map-green-soft) 82%, var(--map-teal) 100%);
  }
  .map-key { position: absolute; left: 14px; top: 668px; width: 18px; height: 14px; background: var(--map-teal); }
  .country-lists { position: absolute; left: 14px; top: 690px; width: 510px; display: flex; gap: 16px; }
  .country-lists p { flex: 1; font-size: 8.5px; line-height: 1.35; color: var(--text); }
  .country-lists b { color: var(--ink); }
</style>
</head>
<body>
<main class="spread">

  <section class="page page-services">
    <h2 class="page-title">OUR SERVICES</h2>

    <div class="globe" role="img" aria-label="Illustrated globe at the centre of the services map"></div>

    <div class="service-icon" style="left:232px;top:118px" role="img" aria-label="Research icon"></div>
    <div class="service" style="left:286px;top:104px;width:210px">
      <h3>Research and analysis of cooperation schemes</h3>
      <p>In Vantor we are convinced that the link between research and practice holds an enormous potential for developing solutions to improve our capacity to achieve collective goals.</p>
    </div>

    <div class="service-icon" style="left:190px;top:168px" role="img" aria-label="Coalition building icon"></div>
    <div class="service" style="left:28px;top:168px;width:150px">
      <h3>Coalition building to achieve collective goals</h3>
      <p>Vantor takes advantage of that large social infrastructure to create well-designed coalitions, partnerships and networks to promote development goals.</p>
    </div>

    <div class="service-icon" style="left:350px;top:214px" role="img" aria-label="Facilitation icon"></div>
    <div class="service" style="left:400px;top:226px;width:126px">
      <h3>Facilitation of processes of change</h3>
      <p>In Vantor we believe that theory cannot be separated from practice. The real background of our work is trying to adapt models to a changing context.</p>
    </div>

    <div class="service-icon" style="left:150px;top:300px" role="img" aria-label="Evaluation icon"></div>
    <div class="service" style="left:24px;top:352px;width:180px">
      <h3>Evaluation of multi-actor projects and programs</h3>
      <p>We follow the Monitoring and Evaluation principles of the Global Development Review Board (GDRB).</p>
    </div>

    <div class="service-icon" style="left:330px;top:392px" role="img" aria-label="Training icon"></div>
    <div class="service" style="left:384px;top:412px;width:142px">
      <h3>Training to improve networked action</h3>
      <p>Our training aims to equip participants with the theoretical and practical tools to approach collaborative schemes in a more effective way.</p>
    </div>

    <div class="service-icon" style="left:302px;top:472px" role="img" aria-label="Methodologies icon"></div>
    <div class="service align-right" style="left:40px;top:430px;width:256px">
      <h3>Methodologies for organizational change<br>and consensus building</h3>
      <p>We prepare a number of complementary products that help to stimulate the reflection and debate of members and, at the same time, can contribute to creating a conducive environment for decision-making within the organization.</p>
    </div>

    <div class="services-band">
      <p>Vantor specializes in the analysis of multi-actor cooperation and the facilitation of processes of change. We believe in the need to improve both the understanding and use of collaborative action. For that, we support value-oriented organisations to integrate a better cooperation logic in their daily practice, whether as part of the internal management process or in the context of their relations with other stakeholders. We see our clients as our most important partners. Through them we learn and improve our knowledge about the challenges of collaborative action. That's why listening carefully to our clients' needs and views is a critical step before designing our interventions. We avoid prefabricated solutions. On the contrary, we engage with them in order to find the right solutions that respond to the needs of the organisation and the requirements of each assignment.</p>
    </div>
  </section>

  <section class="page page-projects">
    <div class="projects-band">
      <p>Vantor started its activities in July 2014. Our previous experience include academic and policy research together with practice in more than a hundred projects in a large number of countries, from some of the poorest and most remote areas of the world to highly developed cities and sectors. In all those we have worked together with a considerable number of relevant organizations and witnessed how effective cooperation becomes a real asset in terms of capacity, resources, visibility, impact and influence.</p>
      <p>Vantor is the result of the collection and examination of all that previous experience. We combine permanently analysis and practice, and incorporate working methods and techniques that encourage active learning and participation.</p>
    </div>
    <h2 class="page-title">OUR PROJECTS</h2>

    <div class="stats">
      <div class="stat"><span class="stat-figure">100+</span><span class="stat-label">PROJECTS</span></div>
      <div class="stat"><span class="stat-figure">75+</span><span class="stat-label">COUNTRIES</span></div>
    </div>

    <div class="world-map" role="img" aria-label="World map highlighting the countries where projects took place"></div>
    <div class="map-key"></div>

    <div class="country-lists">
      <p><b>Europe:</b> EU 28, Norway, Switzerland, Turkey, Montenegro, Ukraine, Serbia, Moldova, Armenia, Georgia and Belarus.<br><b>America:</b> US, Canada, Guatemala, El Salvador, Panamá, Costa Rica, Honduras, Colombia, Peru, Bolivia, Brazil, Argentina, Uruguay and Paraguay.</p>
      <p><b>Asia:</b> China, Vietnam, Thailand, Indonesia, Malaysia, Singapore, Bangladesh, Kyrgyzstan, Kazakhstan and Myanmar.<br><b>Africa:</b> South Africa, Mozambique, Ethiopia, Kenya, Uganda, Benin, Senegal, Zimbabwe, Ghana, Tunisia, Egypt and Libya.</p>
    </div>
  </section>

</main>
</body>
</html>
```